First Birthday Party Invitation

We need a flyer/invitation design for our baby girl Marisol's first birthday party. We want the design to look like a club event flyer. The party will have a sailing/nautical theme and will be at a marina but in Miami so the invite must have a cool, non-baby, non-kitchy vibe.

Here's the text...feel free to play around with it!

Welcome Aboard! 

We'll have lots of fun

Our little Marisol is turning one!

You're invited to a party

on Saturday, August 7th from 5 - 7 p.m.

Tide-And-Rope Miami

Third Floor
4187 North Coralwind Avenue
Miami, FL 33149-7812
Parking tickets will be validated 

Please RSVP by July 31st to MarisolBirthday@bluefinmail.test or 305.482.9067

Arrive early at 4 p.m. to join us on a short pre-party boat tour of the Miami skyline

Flyer should be one-sided only.  It will be printed in color and also emailed. 

Important update - please add small text that says "No gifts please.  A contribution to Tide And Rope's programs would be greatly appreciated."

```html
<!DOCTYPE html>
<html lang="en">
<head>
<meta charset="utf-8">
<title>Marisol's First Birthday – Welcome Aboard</title>
<link rel="stylesheet" href="https://fonts.googleapis.com/css2?family=Arimo:wght@400&family=Fredoka:wght@600&family=Roboto+Condensed:wght@400&family=Rubik:wght@700;800&family=Tinos:wght@400&display=swap">
<style>
  :root {
    --frame-magenta: #9b1a60;
    --panel-black: #050505;
    --text-white: #ffffff;
    --accent-orange: #f7941d;
    --splat-orange: #f0561c;
    --splat-magenta: #b2177a;
    --rsvp-yellow: #f2e33a;
    --swirl-grey: rgba(255, 255, 255, 0.28);
  }
  * { margin: 0; padding: 0; box-sizing: border-box; }
  html, body {
    width: 1200px; height: 900px; overflow: hidden;
    background: #ffffff;
  }
  .invitation {
    position: relative;
    width: 1200px; height: 900px;
    background: var(--frame-magenta);
    overflow: hidden;
  }
  .invitation__panel {
    position: absolute;
    left: 30px; top: 24px; right: 26px; bottom: 48px;
    background: var(--panel-black);
    border-radius: 30px;
    overflow: hidden;
  }
  .line {
    position: absolute;
    line-height: 1;
    white-space: nowrap;
    color: var(--text-white);
  }
  .event-date {
    right: 50px; top: 28px;
    font-family: "Roboto Condensed", "Arial Narrow", sans-serif;
    font-size: 35px;
  }
  .boat-tour {
    right: 44px; top: 68px;
    font-family: "Tinos", "Times New Roman", serif;
    font-size: 26px;
  }
  .welcome {
    left: 320px; top: 198px;
    font-family: "Rubik", "Arial Black", sans-serif;
    font-weight: 800;
    font-variant: small-caps;
    font-size: 64px;
    letter-spacing: 2px;
    z-index: 2;
  }
  .fun-line {
    font-family: "Fredoka", "Arial Rounded MT Bold", sans-serif;
    font-weight: 600;
  }
  .lots-of-fun { left: 80px; top: 290px; font-size: 42px; }
  .turning-one { left: 239px; top: 416px; font-size: 42px; color: var(--accent-orange); }
  .invited { left: 132px; top: 490px; font-size: 46px; }
  .parking { left: 86px; top: 577px; font-size: 36px; }
  .venue {
    position: absolute;
    left: 90px; top: 637px;
    font-family: "Rubik", "Arial", sans-serif;
    font-weight: 700;
    font-variant: small-caps;
    font-size: 28px;
    line-height: 41px;
    color: var(--text-white);
  }
  .rsvp {
    right: 86px; top: 778px;
    font-family: "Tinos", "Times New Roman", serif;
    font-size: 18px;
    letter-spacing: -0.2px;
    color: var(--rsvp-yellow);
    z-index: 2;
  }
  .no-gifts {
    left: 97px; top: 815px;
    font-family: "Arimo", "Arial", sans-serif;
    font-size: 23px;
  }
  .splat {
    position: absolute;
    border-radius: 50%;
  }
  .splat--orange {
    left: 740px; top: 150px; width: 160px; height: 135px;
    background: radial-gradient(circle at 50% 50%, var(--splat-orange) 0 45%, rgba(240, 86, 28, 0) 72%);
    z-index: 1;
  }
  .splat--magenta {
    left: 160px; top: 265px; width: 175px; height: 160px;
    background: radial-gradient(circle at 50% 50%, var(--splat-magenta) 0 45%, rgba(178, 23, 122, 0) 72%);
  }
  .swirl-ornament {
    position: absolute;
    left: 640px; top: 330px; width: 520px; height: 490px;
    border-radius: 0 0 24px 0;
    background: radial-gradient(ellipse at 70% 65%, var(--swirl-grey) 0%, rgba(255, 255, 255, 0.08) 50%, rgba(255, 255, 255, 0) 72%);
  }
</style>
</head>
<body>
  <main class="invitation">
    <div class="invitation__panel"></div>

    <div class="swirl-ornament" role="img" aria-label="White and grey decorative floral swirls"></div>
    <div class="splat splat--magenta" role="img" aria-label="Magenta paint splatter"></div>
    <div class="splat splat--orange" role="img" aria-label="Orange paint splatter"></div>

    <p class="line event-date">On Saturday, August 7th from 5 - 7 p.m.</p>
    <p class="line boat-tour">Arrive early at 4 p.m. to join us on a short pre-party boat tour of the Miami skyline</p>

    <h1 class="line welcome">Welcome Aboard!</h1>

    <p class="line fun-line lots-of-fun">We'll have lots of&nbsp; fun</p>
    <p class="line fun-line turning-one">Our little Marisol is turning one!</p>
    <p class="line fun-line invited">You're invited to a party</p>
    <p class="line fun-line parking">Parking tickets will be validated</p>

    <address class="venue">
      Tide-And-Rope Miami<br>
      Third Floor<br>
      4187 North Coralwind Avenue<br>
      Miami, FL&nbsp; 33149-7812
    </address>

    <p class="line rsvp">Please RSVP by July 31st to MarisolBirthday@bluefinmail.test or 305.482.9067</p>
    <p class="line no-gifts">"No gifts please.&nbsp; A contribution to Tide And Rope's programs would be greatly appreciated."</p>
  </main>
</body>
</html>
```